Web Design Project

i'm looking for a sleek modern design i can use for a web site that deals with.
Clearleaf Capture
Accounts Payable Solutions for faster processing based on our scanning solution.
ultimately we are a intelligent scanning software.

here is a great website, that does exactly what we do, and we like to have most of their services and products.

so something in this idea would be great.
www.varnol.com

so i guess i want a good landing/home page which is smartly designed so users will be inclined to leave their information.

and then information pages.

also i dont need any cms for you to include, i only need you to hook the html hooks for RANK Kettle as i already have a CMS and need it to hook in to that, i am including links to that cheat sheet.
so it is easier when included as you create the Theme.

http://www.rankkettle.com/how-to-create-website-template.html
http://www.rankkettle.com/cheat-sheet.html
Updates

Hi Guys sorry for the long pause in design, but here is where we stand.

what ever design i choose, i need that designer to customize a few things for me based on design that was designed.
and i will need designer to match that them to work with RANK Kettle
here is the cheat sheet for the hooks that we need to match and make it work.
if you have any questions let me know.

otherwise i look forward to working with you. and good luck.

Target Market(s)

CFO's AP Managers, mostly ppl who are not Tech freindly

Industry/Entity Type

Software

Requirements
Must have
• i need on home page, the rotating banner should have 1 ability to place clipvane links to show videos, and also ability to add buttons on these rotating banners that will allow forms to pop up take to another page.

```html
<!DOCTYPE html>
<html lang="en">
<head>
<meta charset="utf-8">
<title>Clearleaf Capture</title>
<link href="https://fonts.googleapis.com/css2?family=Oswald:wght@300;400&display=swap" rel="stylesheet">
<style>
:root{
  --orange:#f39c12;
  --ink:#333333;
  --muted:#555555;
  --line:#bbbbbb;
  --white:#ffffff;
}
*{box-sizing:border-box;margin:0;padding:0}
html,body{width:1200px;height:1182px;overflow:hidden}
body{position:relative;background:linear-gradient(90deg,#bdbdbd 0,#f2f2f2 100px,#fafafa 600px,#f2f2f2 1100px,#c8c8c8 1200px);font-family:Arial,Helvetica,sans-serif;color:var(--ink)}
.page{position:absolute;left:100px;top:0;width:1000px;height:1182px}

.slide-arrow{position:absolute;top:275px;width:50px;height:110px}
.slide-arrow.prev{left:52px;border-radius:55px 0 0 55px;background:#e4e4e4}
.slide-arrow.next{left:1100px;border-radius:0 55px 55px 0;background:#eeeeee}
.slide-arrow svg{position:absolute;top:41px}

.site-header{position:absolute;left:0;top:0;width:1000px;height:105px;background:var(--white);border-bottom:2px solid var(--orange)}
.brand{position:absolute;left:16px;top:34px;font-family:Arial,Helvetica,sans-serif;font-weight:bold;font-size:26px;color:var(--orange);white-space:nowrap}
.search{position:absolute;left:720px;top:11px;width:198px;height:23px;border:1px solid #aaa;border-radius:3px;background:#fff;box-shadow:inset 0 1px 2px rgba(0,0,0,.2)}
.search span{position:absolute;left:8px;top:2px;font-family:'Oswald',sans-serif;font-weight:300;font-size:12px;color:#333}
.search-btn{position:absolute;right:-1px;top:-1px;width:24px;height:23px;background:var(--orange);border-radius:0 3px 3px 0}
.social{position:absolute;top:13px;width:22px;height:22px;border:2px solid #222;border-radius:50%}
.main-nav a{position:absolute;top:79px;font-family:'Oswald',sans-serif;font-weight:300;font-size:14px;color:#222;text-decoration:none;white-space:nowrap}
.main-nav a.active::after{content:"";position:absolute;left:50%;bottom:-9px;margin-left:-5px;border:5px solid transparent;border-bottom-color:var(--orange)}

.hero{position:absolute;left:0;top:105px;width:1000px;height:492px;background:linear-gradient(135deg,#e9eef2 0%,#b9c8d6 35%,#d9cbb8 55%,#9fb2c4 80%,#eef1f3 100%)}
.hero-curve{position:absolute;left:0;top:400px}
.hero-title{position:absolute;left:16px;top:436px;font-family:'Oswald',sans-serif;font-weight:300;font-size:37px;color:#333;letter-spacing:-1px;white-space:nowrap}

.feature{position:absolute;top:598px;height:77px;background:linear-gradient(#ffffff,#e8e8e8);border:1px solid #ddd;font-family:'Oswald',sans-serif}
.feature h3{position:absolute;left:54px;top:12px;font-weight:400;font-size:18px;color:var(--orange)}
.feature p{position:absolute;left:54px;top:41px;font-weight:300;font-size:14.5px;color:#444;white-space:nowrap}

.section-title{font-family:'Oswald',sans-serif;font-weight:400;font-size:17px;color:#222;padding-bottom:9px;border-bottom:1px dashed var(--line);margin-bottom:11px}
.about{position:absolute;left:13px;top:709px;width:416px;font-size:12px;line-height:14.5px;text-align:justify;color:#333}
.about p{margin-bottom:14.5px}
.news{position:absolute;left:479px;top:709px;width:505px;font-size:12px;line-height:14.5px;color:#333;text-align:justify}
.news h4{font-size:12px;color:var(--orange);font-weight:bold;text-align:left}
.news .more{display:block;color:var(--orange);text-decoration:none;margin:15px 0 14px}
.call{position:absolute;left:783px;top:906px;font-family:'Oswald',sans-serif;font-weight:300;font-size:18px;letter-spacing:-.4px;color:#333}

.site-footer{position:absolute;left:0;top:950px;width:1000px;height:232px;background:radial-gradient(circle at 920px 230px,#f2f2f2 0,#e3e3e3 140px,#d6d6d6 300px);border-top:2px solid #bdbdbd}
.footer-title{position:absolute;top:12px;font-family:'Oswald',sans-serif;font-weight:400;font-size:13px;color:#333}
.field{position:absolute;left:23px;width:203px;background:#fff;border:1px solid #999;border-radius:4px;font-size:10px;font-weight:bold;color:#555;padding:6px}
.submit{position:absolute;left:169px;top:192px;width:55px;height:18px;background:var(--orange);border-radius:3px;color:#fff;font-size:11px;font-weight:bold;text-align:center;line-height:18px}
.divider{position:absolute;left:262px;top:30px;width:1px;height:185px;background:#c4c4c4}
.quick{position:absolute;top:49px;list-style:none;font-family:'Oswald',sans-serif;font-weight:300;font-size:12px;color:#333}
.quick li{height:23px}
.quick li::before{content:"› ";color:var(--orange);font-weight:400}
.foot-brand{position:absolute;left:839px;top:112px;font-family:Arial,Helvetica,sans-serif;font-weight:bold;font-size:18px;color:var(--orange);white-space:nowrap}
.copy{position:absolute;left:839px;top:138px;font-family:'Oswald',sans-serif;font-weight:300;font-size:12px;color:#333}
</style>
</head>
<body>
<div class="slide-arrow prev"><svg width="50" height="28" viewBox="0 0 50 28"><path d="M38,2 L28,14 L38,26" fill="none" stroke="#e09a2a" stroke-width="6"/></svg></div>
<div class="slide-arrow next"><svg width="50" height="28" viewBox="0 0 50 28"><path d="M12,2 L22,14 L12,26" fill="none" stroke="#f3b64a" stroke-width="6"/></svg></div>

<div class="page">
  <header class="site-header">
    <div class="brand">Clearleaf Capture</div>
    <div class="search"><span>Search</span>
      <div class="search-btn"><svg width="24" height="23" viewBox="0 0 24 23"><circle cx="11" cy="10" r="4.5" fill="none" stroke="#fff" stroke-width="2"/><line x1="14" y1="13" x2="18" y2="17" stroke="#fff" stroke-width="2.5"/></svg></div>
    </div>
    <span class="social" style="left:937px" aria-label="Social link"></span>
    <span class="social" style="left:965px" aria-label="Social link"></span>
    <nav class="main-nav">
      <a class="active" style="left:472px">Products</a>
      <a style="left:544px">Solutions</a>
      <a style="left:621px">Services</a>
      <a style="left:695px">Partners</a>
      <a style="left:772px">Case Studies</a>
      <a style="left:866px">Our Clients</a>
      <a style="left:951px">Contact</a>
    </nav>
  </header>

  <section class="hero" role="img" aria-label="Photo of three smiling office workers gathered around a laptop">
    <svg class="hero-curve" width="1000" height="92" viewBox="0 0 1000 92">
      <path d="M0,20 Q320,-10 620,92 L0,92 Z" fill="#fff"/>
      <path d="M0,20 Q320,-10 620,92" fill="none" stroke="#f39c12" stroke-width="6"/>
    </svg>
    <h1 class="hero-title">ACCOUNTS PAYABLE SOLUTIONS</h1>
  </section>

  <div class="feature" style="left:0;width:329px"><h3>Five Star Financials</h3><p>Change the game with unbeatable financial apps. »</p></div>
  <div class="feature" style="left:335px;width:329px"><h3 style="left:53px;top:10px">Extreme Visibility</h3><p style="left:53px;top:39px">Get up close and personal with your financial data. »</p></div>
  <div class="feature" style="left:670px;width:330px"><h3 style="left:46px">Infinite Flexibility</h3><p style="left:46px">Get it working for your business. No muscle required. »</p></div>

  <section class="about">
    <h2 class="section-title">CLEARLEAF CAPTURE</h2>
    <p>Clearleaf Capture is a leading document and data capture provider focused on helping organisations drive cost reduction and process improvement within processes such as Accounts Payable. This is achieved through a proven process of understanding and benchmarking current performance, then transforming and automating the current processes to drive cost reduction, incorporating best practices and creating ‘world-class’ performance.</p>
    <p>Clearleaf Capture combines best practice process knowledge and pedigree to a market-leading software suite, enabling organisations to benefit from a complete range of solutions from paper scanning through to intelligent, template-free data extraction and the ability to receipt purchase invoices irrespective of format (EDI, XML, PDF, email).</p>
  </section>

  <section class="news">
    <h2 class="section-title">LATEST NEWS</h2>
    <h4>Clearleaf Capture Shortlisted for National Finance Awards 2012</h4>
    <p>Clearleaf Capture has been shortlisted for the Software Product of the Year category at the prestigious National Finance Awards 2012.</p>
    <a class="more">read more»</a>
    <h4>Hobbs drives Purchase-to-Pay efficiency with "touchless" invoice processing</h4>
    <p>Clearleaf Capture and strategic business partner Norvale Business Software, the UK division of global business software group Norvale, today announced that Hobbs the Bakers has implemented the Billstream hybrid invoice processing solution, delivering 100% of its invoices electronically into Hobbs’s existing Norvale Ledger Financials system.</p>
    <a class="more">read more»</a>
  </section>
  <div class="call">Call us : 555-0142076</div>

  <footer class="site-footer">
    <div class="footer-title" style="left:23px">CONTACT US</div>
    <div class="field" style="top:40px;height:26px">Name</div>
    <div class="field" style="top:75px;height:26px">E-Mail</div>
    <div class="field" style="top:109px;height:77px">Message</div>
    <div class="submit">Submit</div>
    <div class="divider"></div>
    <div class="footer-title" style="left:297px">QUICK LINKS</div>
    <ul class="quick" style="left:290px"><li>Home</li><li>About Us</li><li>Products</li><li>Solutions</li><li>Services</li></ul>
    <ul class="quick" style="left:454px;top:48px"><li>Partners</li><li>Case Studies</li><li>Our Clients</li><li>Contact</li></ul>
    <div class="foot-brand">Clearleaf Capture</div>
    <div class="copy">© Clearleaf Capture 2012</div>
  </footer>
</div>
</body>
</html>
```